Creative Realtor Business Card Design

I need a creative business card.... I would like it to be larger than the normal size...heavy stock.... colorful...
As you are probably aware, there are tons of realtors, and most of their cards ALL look alike.. potential clients are looking for agents that are professional, but are different.
Cards are a form of advertising and I need your help to make mine stand out in a professional, classy way.
I don't need to use the ridgeway meadow realty logo, my personal logo is MORE important for branding purposes. OR..what is your opinion?
YOU DESIGN FOR ME PLEASE! If I could do what you do I would.... I can't and I need your professional help.

                                        If you think I need the card to be double sided so it doesn't look busy by all means I will happily accept double sided. 

I am very interested in a more "creative" card than a standard run of the mill realtor card.    I care about my clients LONG after the sale has closed!

                                   

THANK YOU SO MUCH FOR YOUR EFFORTS AND TALENTS....I APPRECIATE IT SO MUCH! 

                                        Would it be possible to use my theme of my logo to design my card?

                                            Where Every Doorstep Feels Familiar

                              

 

Please make cards larger size .... See this link for ideas that appeal to me. Thank you for your interest.

https://www.lookfindery.example/search?q=examples+of+unique+business+cards&mode=img&ref=7QpLm2VxT9kAzR4bWcYnHe&pg=1

I want my card to stand out in size and design...

Thank you so much for your hard work for me.

Lorna

 

Reason: I learned that many designers are very busy. I am providing more time and money in hopes that designers will find it an attractive enough challenge to participate. My business cards are one of my most important marketing materials...I NEED THEM TO BE DISTINCTIVE, CLASSY, and INFORMATIVE. Thank you SO MUCH....and I will be anxiously awaiting your great designs... Lorna

Hello Designers,

Thank you to all you creative people that have kindly offered to submit your creative design(s) for my business card.  I view your designs as your creative artwork. I am anxious to see where your creativity leads you.

I wanted to share with you that my logo was something I personally designed after being in business for 3  years. ( I did have to have a professionals like yourselves draw it for me). The design and logo captured perfectly how I felt about my work ...helping individuals, such as you, find a home.  A house is easy to find, but a home is a place that has "good" energy ... a place where you feel comfortable and can grow.  A place that just "Feels right!"  It's one of those things that you just KNOW when it is right! 

I hope by sharing this bit of information about me can help you creatively design my card for me...I care for my clients LONG after the transaction has closed and they are in their home. Thank you again for taking the time to work on my design. I have been adding money so that your time spent on my card is worth it.

I do need my card soon...so please, if you have a design...submit it!

Kind Regards,

Lorna

Target Market(s)

I have a variety of clients from a mobile home of $35,000 to an estate property for $5M. I feel comfortable working with all types of people...I love my job...I love helping people find the right home because we all know how our home environment affects our well being.

Industry/Entity Type

Advertising

Contact Information for Business Card

Lorna Packett, Realtor
Ridgeway Meadow Realty
"Where Every Doorstep Feels Familiar"
www.lornaplaces.example
lpackett@mailbrook.example
(555) 418-6032
BRE #04782915, Exp. 8/15

Colors

Designer to choose colors to be used in the design.

Requirements
Must have
• By law, my license number information MUST be on my card.
Nice to have
• I would love card to be memorable...if that is possible for a business card. Also, I would like my card to be larger than the average card. Not sure that is possible either.

```html
<!DOCTYPE html>
<html lang="en">
<head>
<meta charset="utf-8">
<title>Lorna Packett Realtor – Business Card</title>
<link rel="stylesheet" href="https://fonts.googleapis.com/css2?family=Roboto+Condensed:wght@700&family=Roboto:wght@100;300&display=swap">
<style>
  :root {
    --backdrop: #e6e5e8;
    --card: #ffffff;
    --ink-gray: #58585a;
    --brand-red: #c41e2e;
    --brand-green: #1d7a45;
    --thin-ink: #3a3a3c;
  }
  html, body {
    margin: 0;
    width: 1200px;
    height: 900px;
    overflow: hidden;
    background: var(--backdrop);
  }
  .stage {
    position: relative;
    width: 1200px;
    height: 900px;
  }
  .card {
    position: absolute;
    top: 322px;
    width: 520px;
    height: 255px;
  }
  .card--front { left: 60px; }
  .card--back { left: 620px; }
  .card__shape {
    position: absolute;
    inset: 0;
    width: 520px;
    height: 255px;
    overflow: visible;
    filter: drop-shadow(2px 4px 6px rgba(0,0,0,0.25));
  }

  /* Front */
  .wordmark {
    position: absolute;
    left: 18px;
    top: 66px;
    margin: 0;
    font-weight: normal;
    line-height: 1;
  }
  .wordmark__first {
    display: block;
    font-family: "Roboto Condensed", sans-serif;
    font-weight: 700;
    font-size: 90px;
    color: var(--ink-gray);
    letter-spacing: -1px;
  }
  .wordmark__line {
    display: block;
    margin-top: 4px;
    font-size: 52px;
  }
  .wordmark__last {
    font-family: "Roboto Condensed", sans-serif;
    font-weight: 700;
    color: var(--brand-red);
    letter-spacing: -1px;
  }
  .wordmark__title {
    font-family: "Roboto", sans-serif;
    font-weight: 100;
    color: var(--thin-ink);
    margin-left: 4px;
  }

  /* Back */
  .brand-mark {
    position: absolute;
    left: 8px;
    top: 112px;
    width: 140px;
    text-align: center;
    font-family: "Roboto Condensed", sans-serif;
  }
  .brand-mark__tagline {
    font-family: "Roboto", sans-serif;
    font-weight: 300;
    font-size: 8px;
    color: var(--brand-green);
    margin: 0 0 10px;
  }
  .brand-mark__dot {
    display: block;
    width: 46px;
    height: 46px;
    margin: 0 auto 10px;
    border-radius: 50%;
    background: var(--brand-red);
  }
  .brand-mark__name {
    font-weight: 700;
    font-size: 15px;
    color: var(--brand-green);
    letter-spacing: 0.5px;
  }
  .contact {
    position: absolute;
    left: 330px;
    top: 68px;
    color: var(--brand-red);
  }
  .contact__name {
    margin: 0;
    font-family: "Roboto Condensed", sans-serif;
    font-weight: 700;
    font-size: 30px;
    line-height: 1.08;
  }
  .contact__company {
    margin: 4px 0 12px;
    font-family: "Roboto", sans-serif;
    font-weight: 300;
    font-size: 9px;
  }
  .contact__phone {
    display: inline-block;
    padding: 2px 6px;
    border-left: 1px solid var(--brand-red);
    border-right: 1px solid var(--brand-red);
    font-family: "Roboto", sans-serif;
    font-weight: 300;
    font-size: 18px;
    margin-bottom: 10px;
  }
  .contact__details {
    margin: 0;
    font-family: "Roboto", sans-serif;
    font-weight: 300;
    font-size: 10.5px;
    line-height: 1.3;
  }
</style>
</head>
<body>
<main class="stage">

  <section class="card card--front" aria-label="Card front">
    <svg class="card__shape" viewBox="0 0 520 255" aria-hidden="true">
      <path d="M0 10 L365 0 L332 90 L420 42 L515 94 L515 255 L0 255 Z" fill="var(--card)"/>
      <polyline points="232,8 365,3 334,86 420,46 511,96" fill="none" stroke="var(--brand-red)" stroke-width="6" stroke-linejoin="miter"/>
    </svg>
    <h1 class="wordmark">
      <span class="wordmark__first">LORNA</span>
      <span class="wordmark__line"><span class="wordmark__last">PACKETT</span><span class="wordmark__title">REALTOR</span></span>
    </h1>
  </section>

  <section class="card card--back" aria-label="Card back">
    <svg class="card__shape" viewBox="0 0 520 255" aria-hidden="true">
      <path d="M0 110 L78 38 L155 96 L155 0 L515 6 L515 255 L0 255 Z" fill="var(--card)"/>
    </svg>
    <div class="brand-mark">
      <p class="brand-mark__tagline">Where Every Doorstep Feels Familiar</p>
      <span class="brand-mark__dot"></span>
      <div class="brand-mark__name">LORNA PACKETT</div>
    </div>
    <div class="contact">
      <h2 class="contact__name">LORNA<br>PACKETT</h2>
      <p class="contact__company">Realtor Ridgeway Meadow Realty</p>
      <div class="contact__phone">(555) 418-6032</div>
      <p class="contact__details">lpackett@mailbrook.example<br>www.lornaplaces.example<br>BRE #04782915, Exp. 8/15</p>
    </div>
  </section>

</main>
</body>
</html>
```